Pharmacist turned chef in Key West Fl needs a logo design

I am looking for a professional looking business card that says who I am and what I do. For example Chef Dale Morrow, natural organic and health supportive cooking. Phone 305-617-4289 email dalemorrow@quillpost.example web www.thehearthremedy.example, Key West fl. The color or colors should have some green and other colors that look good together that stimulate appetite and give a clean healthy image. To help with a thought process, words like food as medicine, medicine is food, good nutrition is health but at the same time I do not want a lot of medical symbols that me it look clinical. Any questions please contact me.

```html
<!DOCTYPE html>
<html lang="en">
<head>
<meta charset="utf-8">
<title>Chef Dale Morrow – Business Card</title>
<link rel="stylesheet" href="https://fonts.googleapis.com/css2?family=Questrial&display=swap">
<style>
  :root {
    --page-bg: #e9e6e1;
    --card-bg: #ffffff;
    --brand-green: #1f6b3b;
    --soft-green: #85b79b;
    --pepper-red: #d8443f;
    --ink: #151515;
    --muted: #6f8a7b;
    --on-green: #eef3ef;
  }
  * { margin: 0; padding: 0; box-sizing: border-box; }
  html, body {
    width: 1200px;
    height: 800px;
    overflow: hidden;
    background: var(--page-bg);
    font-family: "Questrial", sans-serif;
  }
  .business-card {
    position: absolute;
    left: 50px;
    top: 96px;
    width: 1100px;
    height: 607px;
    background: var(--card-bg);
    overflow: hidden;
    box-shadow: 0 6px 20px rgba(0,0,0,0.18);
  }
  .ground-wave {
    position: absolute;
    inset: 0;
    width: 100%;
    height: 100%;
  }
  .website {
    position: absolute;
    left: 25px;
    top: 22px;
    font-size: 18px;
    letter-spacing: 0.5px;
    color: var(--brand-green);
  }
  .phone {
    position: absolute;
    right: 23px;
    top: 26px;
    font-size: 21px;
    letter-spacing: 1px;
    color: var(--muted);
  }
  .pepper-art {
    position: absolute;
    left: 18px;
    top: 167px;
    width: 138px;
    height: 276px;
    border-radius: 44% 40% 46% 42%;
    background: radial-gradient(circle at 40% 40%, #e45a52, var(--pepper-red) 60%, #b8322f);
  }
  .cutlery-art {
    position: absolute;
    left: 810px;
    top: 132px;
    width: 228px;
    height: 318px;
    border-radius: 50% 50% 8px 8px / 30% 30% 8px 8px;
    background: linear-gradient(160deg, #9ccab0, var(--soft-green));
    opacity: 0.85;
  }
  .identity {
    position: absolute;
    left: 172px;
    top: 246px;
    width: 620px;
  }
  .chef-name {
    font-size: 57px;
    font-weight: 400;
    letter-spacing: 1px;
    line-height: 1;
    white-space: nowrap;
    color: var(--ink);
  }
  .tagline {
    margin-top: 12px;
    font-size: 30px;
    line-height: 1.1;
    white-space: nowrap;
    color: var(--ink);
  }
  .tagline .accent { color: var(--brand-green); }
  .email {
    position: absolute;
    right: 28px;
    bottom: 22px;
    font-size: 21px;
    color: var(--on-green);
  }
</style>
</head>
<body>
  <article class="business-card">
    <svg class="ground-wave" viewBox="0 0 1100 607" preserveAspectRatio="none" aria-hidden="true">
      <path fill="var(--brand-green)" d="M0,532 C160,500 480,455 700,447 C880,441 1020,446 1100,452 L1100,607 L0,607 Z"/>
      <path fill="var(--card-bg)" d="M0,548 C50,540 110,540 118,556 C124,570 70,580 0,580 Z"/>
    </svg>

    <p class="website">www.thehearthremedy.example</p>
    <p class="phone">P: 305-617-4289</p>

    <div class="pepper-art" role="img" aria-label="Illustration of red bell peppers"></div>
    <div class="cutlery-art" role="img" aria-label="Illustration of a fork and knife"></div>

    <header class="identity">
      <h1 class="chef-name">CHEF DALE MORROW</h1>
      <p class="tagline">Natural <span class="accent">Organic</span> &amp; <span class="accent">Health</span> Supportive Cook</p>
    </header>

    <p class="email">dalemorrow@quillpost.example</p>
  </article>
</body>
</html>
```